RTW Business Card Design

We are an independent auto dealer who specializes in commercial & fleet vehicles, we are family owned and operated and have been in business since 2001. We stock late model, low mileage, white trucks & vans. We mostly deal with companies in the construction and service industries. We are just looking to try to freshen up our old business card, we do not want to change the logo at this point, because it is well know within the southwest region & construction community. I have attached our logo and a PDF of our current business card for reference.
Updates
If the address is stacked there is no comma (,) after NE. Everyone keeps putting it in with this format and it is not correct.
842 Ventana Blvd NE
Albuquerque, NM 87120
If the address is all on one line, then there will be a comma (,) after NE
842 Ventana Blvd NE, Albuquerque, NM 87120
Please make changes accordingly, thank you for your attention in this matter.
Industry/Entity Type
Construction
Contact Information for Business Card
842 Ventana Blvd NE, Albuquerque, NM 87120, Marcus Delaney, Vice President, marcus@rtwvehicledepot.com, www.RTWvehicledepot.com, ph 505-610-2247, fax 505-472-8156, cell 505-238-6094
Look and feel
Each slider illustrates characteristics of the customer's brand and the style your logo design should communicate.

```html
<!DOCTYPE html>
<html lang="en">
<head>
<meta charset="utf-8">
<title>RTW Vehicle Depot – Stationery</title>
<link rel="stylesheet" href="https://fonts.googleapis.com/css2?family=Playfair+Display:wght@700&family=Marcellus+SC&family=Open+Sans:wght@400;600&display=swap">
<style>
  :root{
    --stage:#b6c3cc;
    --paper:#ffffff;
    --ink:#1c1c1c;
    --red:#e2232a;
    --black:#111111;
    --grey:#444444;
    --faint:#e6e6e6;
  }
  *{box-sizing:border-box;margin:0;padding:0}
  html,body{width:1200px;height:575px;overflow:hidden}
  body{background:var(--stage);position:relative;font-family:"Open Sans",Arial,sans-serif;color:var(--ink)}

  .sheet{position:absolute;background:var(--paper);box-shadow:0 3px 10px rgba(0,0,0,.28);overflow:hidden}
  .business-card{left:40px;top:98px;width:317px;height:182px}
  .envelope{left:13px;top:353px;width:369px;height:167px}
  .letterhead{left:402px;top:25px;width:382px;height:524px}
  .letterhead-blank{left:803px;top:25px;width:382px;height:524px}

  .brand{position:absolute;font-family:"Playfair Display",Georgia,serif;font-weight:700;color:var(--ink);line-height:.9;letter-spacing:.5px}
  .brand__name{display:block}
  .brand__sub{display:block}

  .business-card .brand{left:21px;top:22px}
  .business-card .brand__name{font-size:30px}
  .business-card .brand__sub{font-size:13px}
  .envelope .brand{left:15px;top:12px}
  .envelope .brand__name{font-size:22px}
  .envelope .brand__sub{font-size:9.5px}
  .letterhead .brand{left:23px;top:17px}
  .letterhead .brand__name{font-size:30px}
  .letterhead .brand__sub{font-size:13px}
  .letterhead-blank .brand{left:0;right:0;top:17px;text-align:center}
  .letterhead-blank .brand__name{font-size:30px}
  .letterhead-blank .brand__sub{font-size:13px}

  .watermark{position:absolute;left:0;right:0;top:200px;text-align:center;font-family:"Playfair Display",Georgia,serif;font-weight:700;color:var(--faint);line-height:.9}
  .watermark .brand__name{font-size:84px}
  .watermark .brand__sub{font-size:34px}

  .smallcaps{font-family:"Marcellus SC",Georgia,serif}
  .holder{position:absolute;right:19px;top:78px;text-align:right}
  .holder__name{color:var(--red);font-size:11.5px;font-weight:700;letter-spacing:.4px}
  .holder__title{font-size:8.5px;color:var(--grey)}
  .rule{position:absolute;left:21px;right:19px;top:106px;height:1.5px;background:var(--black)}

  .contacts{position:absolute;list-style:none;font-family:"Marcellus SC",Georgia,serif;color:var(--ink)}
  .contacts li{display:flex;align-items:center;gap:5px}
  .contacts svg{fill:var(--red);flex:none}
  .business-card .contacts{left:21px;top:118px;font-size:8px;line-height:11px}
  .business-card .contacts svg{width:7px;height:7px}
  .envelope .contacts{left:15px;top:68px;font-size:5.5px;line-height:7px;gap:3px}
  .envelope .contacts li{gap:3px}
  .envelope .contacts svg{width:5px;height:5px}
  .letterhead .contacts{right:14px;top:21px;font-size:8px;line-height:10px;text-align:right}
  .letterhead .contacts li{justify-content:flex-end;gap:6px}
  .letterhead .contacts svg{width:7px;height:7px}
  .holder-repeat{position:absolute;right:19px;top:118px;text-align:right;font-family:"Marcellus SC",Georgia,serif;font-size:8px;line-height:11px}

  .footer-band{position:absolute;left:0;bottom:0;width:100%}
  .footer-url{position:absolute;color:#fff;font-family:"Marcellus SC",Georgia,serif;white-space:nowrap}
  .business-card .footer-url{right:10px;bottom:4px;font-size:7.5px}
  .envelope .footer-url{right:12px;bottom:5px;font-size:6.5px}
  .letterhead .footer-url{right:10px;bottom:6px;font-size:7.5px}

  .letter{position:absolute;left:39px;top:125px;width:332px;font-size:6.3px;line-height:8.4px;color:#333}
  .letter p{margin-bottom:8px}
  .letter .recipient{margin-bottom:9px}
  .signature{display:flex;align-items:center;gap:6px;margin-top:14px}
  .signature__mark{width:38px;height:16px;background:linear-gradient(90deg,#c9c3dc,#8e86b3);border-radius:8px}
  .signature__seal{width:34px;height:34px;border-radius:50%;background:#d4e8ef;border:1px solid #a9cfdb}
</style>
</head>
<body>

<svg width="0" height="0" style="position:absolute" aria-hidden="true">
  <defs>
    <symbol id="ico-mobile" viewBox="0 0 10 10"><rect x="2.5" y="0" width="5" height="10" rx="1"/><rect x="3.3" y="1.2" width="3.4" height="6" fill="#fff"/></symbol>
    <symbol id="ico-phone" viewBox="0 0 10 10"><path d="M0 4 Q5 0 10 4 L9 5.5 7 4.5 7 3.5 Q5 2.8 3 3.5 L3 4.5 1 5.5Z"/><rect x="2" y="5.5" width="6" height="4" rx=".6"/></symbol>
    <symbol id="ico-fax" viewBox="0 0 10 10"><rect x="2.5" y="0" width="5" height="4"/><rect x="0" y="3.5" width="10" height="4.5" rx=".8"/><rect x="2.5" y="7" width="5" height="3"/></symbol>
    <symbol id="ico-mail" viewBox="0 0 10 10"><rect x="0" y="1.5" width="10" height="7" rx=".6"/><path d="M.5 2 5 5.5 9.5 2" stroke="#fff" stroke-width="1" fill="none"/></symbol>
  </defs>
</svg>

<!-- Business card -->
<section class="sheet business-card">
  <div class="brand"><span class="brand__name">RTW</span><span class="brand__sub">VEHICLE DEPOT</span></div>
  <div class="holder smallcaps">
    <div class="holder__name">Marcus Delaney</div>
    <div class="holder__title">Vice President</div>
  </div>
  <div class="rule"></div>
  <ul class="contacts">
    <li><svg><use href="#ico-mobile"/></svg>505-610-2247</li>
    <li><svg><use href="#ico-phone"/></svg>505-472-8156</li>
    <li><svg><use href="#ico-fax"/></svg>505-238-6094</li>
    <li><svg><use href="#ico-mail"/></svg>marcus@rtwvehicledepot.com</li>
  </ul>
  <div class="holder-repeat">Marcus Delaney<br>Vice President</div>
  <svg class="footer-band" width="317" height="18" viewBox="0 0 317 18">
    <rect x="0" y="8" width="317" height="10" fill="var(--black)"/>
    <polygon points="208,18 218,2 317,2 317,18" fill="#fff"/>
    <polygon points="212,18 221,4 317,4 317,18" fill="var(--red)"/>
  </svg>
  <span class="footer-url">www.RTWvehicledepot.com</span>
</section>

<!-- Envelope -->
<section class="sheet envelope">
  <div class="brand"><span class="brand__name">RTW</span><span class="brand__sub">VEHICLE DEPOT</span></div>
  <ul class="contacts">
    <li><svg><use href="#ico-mobile"/></svg>505-610-2247</li>
    <li><svg><use href="#ico-phone"/></svg>505-472-8156</li>
    <li><svg><use href="#ico-fax"/></svg>505-238-6094</li>
    <li><svg><use href="#ico-mail"/></svg>marcus@rtwvehicledepot.com</li>
  </ul>
  <svg class="footer-band" width="369" height="20" viewBox="0 0 369 20">
    <rect x="0" y="10" width="369" height="10" fill="var(--black)"/>
    <polygon points="240,20 252,1 369,1 369,20" fill="#fff"/>
    <polygon points="245,20 256,3 369,3 369,20" fill="var(--red)"/>
  </svg>
  <span class="footer-url">www.RTWvehicledepot.com</span>
</section>

<!-- Letterhead with letter -->
<section class="sheet letterhead">
  <div class="brand"><span class="brand__name">RTW</span><span class="brand__sub">VEHICLE DEPOT</span></div>
  <ul class="contacts">
    <li>505-610-2247<svg><use href="#ico-mobile"/></svg></li>
    <li>505-472-8156<svg><use href="#ico-phone"/></svg></li>
    <li>505-238-6094<svg><use href="#ico-fax"/></svg></li>
    <li>marcus@rtwvehicledepot.com<svg><use href="#ico-mail"/></svg></li>
  </ul>
  <div class="watermark" aria-hidden="true"><span class="brand__name">RTW</span><span class="brand__sub">VEHICLE DEPOT</span></div>
  <article class="letter">
    <p class="recipient">Someone Somebody<br>100 Long St<br>Brisbane, Australia</p>
    <p>Dear Someone Somebody,</p>
    <p>Lorem ipsum dolor sit amet, consectetuer adipiscing elit. Praesent mattis eros a tellus. Quisque leo tortor, commodo id, dapibus et, lacinia et, justo. Ut urna sapien, dictum eu, cursus vel, consectetuer tincidunt, eros. Etiam in libero. Etiam tempor. Maecenas ligula felis, commodo eget, scelerisque id, suscipit nec, odio. Vivamus commodo, magna in mollis feugiat, felis nisl dapibus dolor, eu blandit orci nulla in orci. Cras felis ipsum, mollis at, semper et, tincidunt id, ipsum. Ut consectetuer elit nec elit. Cras luctus molestie ligula. In gravida tempor nunc.</p>
    <p>Curabitur nisl ligula, pulvinar et, volutpat non, porta a, ipsum. Donec tristique ante at est. Pellentesque volutpat est non diam. Aenean vel velit. Suspendisse facilisis nisl et massa. Mauris nec erat. Pellentesque luctus arcu ut dui. Proin suscipit lorem id augue. Maecenas eget ipsum nec orci convallis viverra. Suspendisse potenti. Donec sed enim. Ut et turpis. Ut mattis enim nec nisl. Ut quam. Pellentesque lobortis vehicula risus.</p>
    <p>Etiam massa erat, tempor et, elementum fringilla, pellentesque ac, odio. Cras sed felis. Aliquam erat volutpat. Etiam tristique. Donec pellentesque, nulla semper adipiscing faucibus, nibh augue semper sapien, eget feugiat dui massa et urna. Nullam ac arcu. Quisque interdum. Morbi tristique sagittis arcu. Phasellus euismod ante eget risus. Nam convallis rutrum augue. Pellentesque placerat ultrices tellus.</p>
    <p>Your Sincerely,<br>Owen Hartley.</p>
    <div class="signature">
      <div class="signature__mark" role="img" aria-label="Handwritten signature"></div>
      <div class="signature__seal" role="img" aria-label="Company seal"></div>
    </div>
  </article>
  <svg class="footer-band" width="382" height="22" viewBox="0 0 382 22">
    <rect x="0" y="13" width="382" height="9" fill="var(--black)"/>
    <polygon points="252,22 266,0 382,0 382,22" fill="#fff"/>
    <polygon points="257,22 270,2 382,2 382,22" fill="var(--red)"/>
  </svg>
  <span class="footer-url">www.RTWvehicledepot.com</span>
</section>

<!-- Blank letterhead -->
<section class="sheet letterhead-blank">
  <div class="brand"><span class="brand__name">RTW</span><span class="brand__sub">VEHICLE DEPOT</span></div>
  <div class="watermark" aria-hidden="true"><span class="brand__name">RTW</span><span class="brand__sub">VEHICLE DEPOT</span></div>
  <svg class="footer-band" width="382" height="22" viewBox="0 0 382 22">
    <rect x="0" y="13" width="382" height="9" fill="var(--black)"/>
    <polygon points="252,22 266,0 382,0 382,22" fill="#fff"/>
    <polygon points="257,22 270,2 382,2 382,22" fill="var(--red)"/>
  </svg>
</section>

</body>
</html>
```